Business Consulting Company needs a business card designed

We need a business card in Brisbane Australia for a company called " Marrowvale Consulting Group". I would like to see the designs either in purple or green color

```html
<!DOCTYPE html>
<html lang="en">
<head>
<meta charset="utf-8">
<title>Marrowvale Consulting Group – Business Card</title>
<link href="https://fonts.googleapis.com/css2?family=Oswald:wght@500&family=Roboto:wght@400;500;700&display=swap" rel="stylesheet">
<style>
  :root {
    --page-bg: #eceae6;
    --card-white: #ffffff;
    --card-shade: #e9eaec;
    --brand-green: #2f9a5a;
    --ink-dark: #2e2e30;
    --ink-grey: #6b6d70;
    --rule-grey: #a9abae;
    --icon-bg: #3a3b3d;
  }
  * { margin: 0; padding: 0; box-sizing: border-box; }
  html, body { width: 1057px; height: 1200px; overflow: hidden; }
  body {
    background: var(--page-bg);
    font-family: "Roboto", Arial, sans-serif;
    position: relative;
  }
  .card {
    position: absolute;
    left: 118px;
    width: 820px;
    height: 470px;
    background: radial-gradient(ellipse at 40% 35%, var(--card-white) 0%, var(--card-white) 45%, var(--card-shade) 100%);
    box-shadow: 0 10px 28px rgba(0,0,0,0.18);
    overflow: hidden;
  }
  .card--front { top: 75px; }
  .card--back { top: 655px; }

  .brand-band {
    position: absolute;
    left: 0; right: 0; bottom: 52px;
    height: 44px;
    background: var(--brand-green);
    color: #fff;
    display: flex;
    align-items: center;
    justify-content: center;
    font-size: 17px;
    letter-spacing: 3px;
  }

  .wordmark {
    position: absolute;
    display: flex;
    align-items: center;
    gap: 16px;
    color: var(--brand-green);
    font-weight: 700;
    line-height: 1.1;
  }
  .wordmark__square {
    width: 46px; height: 46px;
    background: var(--brand-green);
    flex: none;
  }
  .card--front .wordmark { left: 230px; top: 140px; font-size: 38px; }
  .card--back .wordmark { left: 60px; top: 250px; font-size: 30px; }
  .card--back .wordmark__square { width: 38px; height: 38px; }

  .dividers { position: absolute; inset: 0; }
  .dividers line { stroke: var(--rule-grey); stroke-width: 4; }

  .person { position: absolute; left: 70px; top: 48px; }
  .person__name {
    font-family: "Oswald", "Arial Narrow", sans-serif;
    font-weight: 500;
    font-size: 40px;
    letter-spacing: 1px;
    color: var(--ink-dark);
  }
  .person__title {
    font-size: 15px;
    letter-spacing: 3px;
    color: var(--ink-grey);
    margin-top: 2px;
  }

  .contacts {
    position: absolute;
    left: 470px; top: 60px;
    list-style: none;
    display: flex;
    flex-direction: column;
    gap: 14px;
  }
  .contacts__item {
    display: flex;
    align-items: center;
    gap: 12px;
    font-size: 16px;
    color: var(--ink-grey);
  }
  .contacts__icon { width: 24px; height: 24px; flex: none; }
  .contacts__icon .icon-bg { fill: var(--icon-bg); }
</style>
</head>
<body>

  <section class="card card--front" aria-label="Card front">
    <div class="wordmark">
      <span class="wordmark__square"></span>
      <span>Marrowvale<br>Consulting Group</span>
    </div>
    <div class="brand-band">www.marrowvaleconsulting.com</div>
  </section>

  <section class="card card--back" aria-label="Card back">
    <svg class="dividers" width="820" height="470" viewBox="0 0 820 470" aria-hidden="true">
      <line x1="60" y1="150" x2="400" y2="150"/>
      <line x1="440" y1="30" x2="440" y2="360"/>
    </svg>

    <div class="person">
      <div class="person__name">DANIEL HARROW</div>
      <div class="person__title">GENERAL MANAGER</div>
    </div>

    <ul class="contacts">
      <li class="contacts__item">
        <svg class="contacts__icon" viewBox="0 0 24 24" aria-hidden="true"><rect class="icon-bg" width="24" height="24" rx="3"/><path d="M8 6l2 3-1.5 1.5a8 8 0 0 0 5 5L15 14l3 2-1 2c-5 0-11-6-11-11z" fill="#fff"/></svg>
        <span>07 3164 2290</span>
      </li>
      <li class="contacts__item">
        <svg class="contacts__icon" viewBox="0 0 24 24" aria-hidden="true"><rect class="icon-bg" width="24" height="24" rx="3"/><rect x="8" y="5" width="8" height="14" rx="1.5" fill="none" stroke="#fff" stroke-width="1.8"/><circle cx="12" cy="16.5" r="1" fill="#fff"/></svg>
        <span>07 3164 2291</span>
      </li>
      <li class="contacts__item">
        <svg class="contacts__icon" viewBox="0 0 24 24" aria-hidden="true"><rect class="icon-bg" width="24" height="24" rx="3"/><rect x="5" y="7" width="14" height="10" fill="none" stroke="#fff" stroke-width="1.6"/><path d="M5 7l7 6 7-6" fill="none" stroke="#fff" stroke-width="1.6"/></svg>
        <span>d.harrow@marrowvale.com</span>
      </li>
      <li class="contacts__item">
        <svg class="contacts__icon" viewBox="0 0 24 24" aria-hidden="true"><rect class="icon-bg" width="24" height="24" rx="3"/><circle cx="12" cy="12" r="6.5" fill="none" stroke="#fff" stroke-width="1.5"/><path d="M5.5 12h13M12 5.5c-3 3.5-3 9.5 0 13M12 5.5c3 3.5 3 9.5 0 13" fill="none" stroke="#fff" stroke-width="1.3"/></svg>
        <span>www.marrowvaleconsulting.com</span>
      </li>
    </ul>

    <div class="wordmark">
      <span class="wordmark__square"></span>
      <span>Marrowvale<br>Consulting Group</span>
    </div>

    <div class="brand-band">27 Kestrel Lane, Level 3, Brisbane</div>
  </section>

</body>
</html>
```